I want a CD cover for a single release that incorporates my photo. Simple classy and beautiful. I have attached my photo and a clip of the video. The artwork should include my name, Darnell Hovey and the title of the song "Rise Up Tonight". I also would like to use this for other promos so in designing where you put the title of the song, it can be replaced with another title.
Target Market(s)
Gospel Music Industry

```html
<!DOCTYPE html>
<html lang="en">
<head>
<meta charset="utf-8">
<title>Darnell Hovey – Rise Up Tonight</title>
<link href="https://fonts.googleapis.com/css2?family=Big+Shoulders+Display:wght@500&family=Montserrat:wght@600&display=swap" rel="stylesheet">
<style>
  :root {
    --bg-top: #2b5467;
    --bg-mid: #234656;
    --bg-bottom: #2f5e77;
    --title-1: #0c1c25;
    --title-2: #1a3342;
    --title-3: #20404f;
    --title-4: #2a5166;
    --title-5: #3a6b86;
    --photo-light: #8a8a8a;
    --photo-dark: #1a1a1a;
    --name: #ffffff;
  }
  html, body {
    margin: 0;
    padding: 0;
    width: 1200px;
    height: 1200px;
    overflow: hidden;
  }
  .cover {
    position: relative;
    width: 1200px;
    height: 1200px;
    background: radial-gradient(ellipse at 50% 55%, var(--bg-mid) 0%, transparent 70%),
                linear-gradient(180deg, var(--bg-top) 0%, var(--bg-mid) 50%, var(--bg-bottom) 100%);
    overflow: hidden;
  }
  .title-stack {
    position: absolute;
    inset: 0;
  }
  .title-row {
    font-family: "Big Shoulders Display", "Oswald", sans-serif;
    font-weight: 500;
    font-size: 282px;
    text-transform: uppercase;
  }
  .title-row--1 { fill: var(--title-1); }
  .title-row--2 { fill: var(--title-2); }
  .title-row--3 { fill: var(--title-3); }
  .title-row--4 { fill: var(--title-4); }
  .title-row--5 { fill: var(--title-5); }
  .artist-photo {
    position: absolute;
    left: 339px;
    top: 248px;
    width: 521px;
    height: 783px;
    background: linear-gradient(180deg, var(--photo-light) 0%, #4a4a4a 35%, var(--photo-dark) 70%, #0c0c0c 100%);
  }
  .artist-name {
    position: absolute;
    left: 0;
    right: 0;
    top: 578px;
    margin: 0;
    text-align: center;
    font-family: "Montserrat", sans-serif;
    font-weight: 600;
    font-size: 37px;
    letter-spacing: 0.95em;
    padding-left: 0.95em;
    color: var(--name);
    text-transform: uppercase;
  }
</style>
</head>
<body>
  <main class="cover">
    <svg class="title-stack" width="1200" height="1200" viewBox="0 0 1200 1200" aria-label="Rise Up Tonight">
      <text class="title-row title-row--1" x="85" y="264" textLength="1033" lengthAdjust="spacingAndGlyphs">Rise Up Tonight</text>
      <text class="title-row title-row--2" x="85" y="481" textLength="1033" lengthAdjust="spacingAndGlyphs">Rise Up Tonight</text>
      <text class="title-row title-row--3" x="85" y="698" textLength="1033" lengthAdjust="spacingAndGlyphs">Rise Up Tonight</text>
      <text class="title-row title-row--4" x="85" y="916" textLength="1033" lengthAdjust="spacingAndGlyphs">Rise Up Tonight</text>
      <text class="title-row title-row--5" x="85" y="1134" textLength="1033" lengthAdjust="spacingAndGlyphs">Rise Up Tonight</text>
    </svg>
    <div class="artist-photo" role="img" aria-label="Portrait of the artist in a black vest and turtleneck wearing a cross pendant, against a grey studio backdrop"></div>
    <h1 class="artist-name">Darnell Hovey</h1>
  </main>
</body>
</html>
```